KM Estates Stationary/Letterhead for customer mail out

I need letterhead for my real estate company which I will use to send promotional mailers out to new potential customers. The realty company is in the St. Paul Michigan area, and we sell commercial real estate, mostly apartment development, and we focus on higher income clients. The letterhead should be modern and appealing to a wealthy demographic.

Target Market(s)

Urban, wealthier demographic of men and women working in the metropolitan St. Paul area.

Industry/Entity Type

Real Estate Development

Requirements
Must have
• Striking appeal. No more than 3 colors. "KM" should be spelled out as if they were signature in handwriting, rather than a standard font-set.
Should not have
• Don't use cursive writing.

```html
<!DOCTYPE html>
<html lang="en">
<head>
<meta charset="utf-8">
<title>KM Estates Stationery</title>
<link href="https://fonts.googleapis.com/css2?family=Open+Sans:wght@400;600;700&display=swap" rel="stylesheet">
<style>
  :root {
    --backdrop: #e6e4e1;
    --paper: #ffffff;
    --ink: #4a4a4a;
    --ink-soft: #7a7a7a;
    --card-dark: #0d0d0d;
    --card-dark-text: #8a8a8a;
    --flap-grey: #5e5e5e;
  }
  * { box-sizing: border-box; margin: 0; padding: 0; }
  html, body { width: 900px; height: 1200px; overflow: hidden; }
  body {
    background: var(--backdrop);
    font-family: "Open Sans", Arial, sans-serif;
    color: var(--ink);
    position: relative;
  }
  .sheet { position: absolute; background: var(--paper); box-shadow: 0 2px 6px rgba(0,0,0,.18); }

  .brand-name { font-weight: 700; color: var(--ink); white-space: nowrap; line-height: 1; }

  /* letterhead */
  .letterhead { left: 171px; top: 40px; width: 558px; height: 636px; padding: 62px 42px 0 42px; font-size: 6.5px; line-height: 10px; }
  .letterhead .brand-name { position: absolute; right: 42px; top: 92px; font-size: 18px; }
  .recipient { margin-top: 34px; }
  .salutation { margin-top: 122px; font-weight: 700; }
  .letter-body p { margin-top: 10px; text-align: justify; color: var(--ink-soft); }
  .sign-off { margin-top: 52px; text-align: right; }
  .letter-footer { position: absolute; right: 42px; bottom: 24px; text-align: right; font-size: 5.5px; line-height: 9px; color: var(--ink-soft); }

  /* business cards */
  .card { top: 729px; width: 228px; height: 120px; }
  .card-front { left: 210px; }
  .card-front .brand-name { position: absolute; left: 16px; top: 70px; font-size: 12px; }
  .card-contact { position: absolute; left: 122px; top: 16px; font-size: 5.5px; line-height: 8.5px; }
  .card-contact .person { font-weight: 700; font-size: 6.5px; margin-bottom: 12px; }
  .card-back { left: 450px; background: var(--card-dark); display: flex; align-items: center; justify-content: center; }
  .card-back .brand-name { color: var(--card-dark-text); font-size: 15px; }

  /* envelope */
  .envelope { left: 219px; top: 900px; width: 465px; height: 264px; }
  .envelope-flap { position: absolute; left: 0; top: 0; width: 100%; height: 36px; }
  .flap-text { position: absolute; right: 22px; top: 13px; color: #fff; font-size: 5.5px; white-space: nowrap; }
  .envelope .brand-name { position: absolute; left: 30px; top: 134px; font-size: 18px; }
  .address-window { position: absolute; left: 216px; top: 114px; width: 210px; height: 66px; border: 1px solid #b8b8b8; border-radius: 8px; padding: 10px 12px; font-size: 7px; color: var(--ink-soft); }
</style>
</head>
<body>

<section class="sheet letterhead">
  <p class="brand-name">KM Estates</p>
  <p class="letter-date">March 12, 2024</p>
  <div class="recipient">
    <p>To</p>
    <p>Avery Collins</p>
    <p>Northgate Holdings</p>
    <p>PO Box 2210, Saint Paul, MN 55102</p>
  </div>
  <p class="salutation">Dear Sir,</p>
  <div class="letter-body">
    <p>Thank you for your interest in our growing portfolio of residential and commercial properties across the greater Saint Paul area. Over the past decade our team has guided private investors, developers and families through the purchase of apartment buildings, mixed-use blocks and premium homes in the most desirable neighborhoods of the city. We believe every client deserves clear advice, honest numbers and a partner who treats each decision with care. Our advisors study each market closely, from rental demand to planned transit and new retail, so that every acquisition is built on solid ground and long-term value.</p>
    <p>Enclosed you will find a short overview of our current listings together with several new development sites that will be offered to select clients before they reach the open market this season.</p>
    <p>We would welcome the chance to meet with you in person to discuss your goals, whether you are expanding an existing portfolio or considering your first investment in multifamily housing. A private consultation takes less than an hour and carries no obligation. Our office is open on weekdays, and evening appointments can be arranged on request.</p>
    <p>We look forward to hearing from you and to helping you find the right property for the years ahead.</p>
  </div>
  <p class="sign-off">Dana Mercer</p>
  <div class="letter-footer">
    <p>120 Harbor Street, Suite 4, Saint Paul, MN 55101</p>
    <p>T: (651) 555-0142 &nbsp;|&nbsp; F: (651) 555-0143 &nbsp;|&nbsp; E: office@kmestates.com</p>
  </div>
</section>

<section class="sheet card card-front">
  <p class="brand-name">KM Estates</p>
  <div class="card-contact">
    <p class="person">Dana Mercer</p>
    <p>T: (651) 555-0142</p>
    <p>F: (651) 555-0143</p>
    <p>M: (651) 555-0198</p>
    <p>office@kmestates.com</p>
    <p>www.kmestates.com</p>
  </div>
</section>

<section class="sheet card card-back">
  <p class="brand-name">KM Estates</p>
</section>

<section class="sheet envelope">
  <svg class="envelope-flap" viewBox="0 0 465 36" preserveAspectRatio="none" aria-hidden="true">
    <polygon points="0,0 465,0 465,36 34,36 0,10" fill="var(--flap-grey)"/>
  </svg>
  <p class="flap-text">120 Harbor Street, Suite 4, Saint Paul, MN 55101 &nbsp;|&nbsp; T: (651) 555-0142 &nbsp;|&nbsp; www.kmestates.com</p>
  <p class="brand-name">KM Estates</p>
  <div class="address-window">To</div>
</section>

</body>
</html>
```